Business Card Design - TORVEX
miles@torvex.example
Project: Business Card Design - TORVEX
Business Card Design - TORVEX - Telecommunications
Creative Brief
Professional
Miles Brandt
Vice President
www.torvex.example
Looking for a very well designed and eye catching business card that we can use into the future. Should be designed around the TORVEX logo and using the included radio images is just optional.
Digital Communications Coastline Fleet Relay Grid Cellphone Coverage Enhancement P25 - Public Safety Equipment Digital Radio Rentals Dispatch Consoles
milestor7 milestor7
Thanks for all the design ideas so far. I will be getting together with my team and will start providing feedback this afternoon. Best Wishes, Miles

```html
<!DOCTYPE html>
<html lang="en">
<head>
<meta charset="utf-8">
<title>TORVEX Business Card</title>
<link rel="stylesheet" href="https://fonts.googleapis.com/css2?family=Michroma&display=swap">
<style>
  :root {
    --bg: #e9e6e1;
    --card: #ffffff;
    --ink: #2a2a2a;
    --red: #d3202a;
    --radio-dark: #2b2d30;
    --radio-mid: #5a5d62;
    --shadow: rgba(0,0,0,0.18);
  }
  * { margin: 0; padding: 0; box-sizing: border-box; }
  html, body { width: 1200px; height: 901px; overflow: hidden; }
  body {
    background: var(--bg);
    font-family: "Michroma", "Arial", sans-serif;
    color: var(--ink);
    display: flex;
    align-items: center;
    justify-content: center;
    gap: 40px;
  }
  .card {
    position: relative;
    width: 520px;
    height: 297px;
    background: var(--card);
    box-shadow: 0 10px 28px var(--shadow);
    overflow: hidden;
  }
  .wordmark {
    font-size: 40px;
    letter-spacing: 6px;
    color: var(--ink);
    line-height: 1;
  }
  .radio-image {
    position: absolute;
    background: linear-gradient(160deg, var(--radio-mid), var(--radio-dark));
    border-radius: 8px;
  }

  /* front */
  .card-front .wordmark { position: absolute; left: 36px; top: 40px; }
  .contact-block { position: absolute; left: 36px; top: 128px; }
  .person-name { font-size: 14px; letter-spacing: 2px; text-transform: uppercase; }
  .person-title { font-size: 11px; letter-spacing: 2px; text-transform: uppercase; color: var(--red); margin-top: 4px; margin-bottom: 12px; }
  .contact-line { display: flex; align-items: center; gap: 8px; font-size: 10px; letter-spacing: 1px; text-transform: uppercase; margin-top: 7px; }
  .contact-line svg { width: 12px; height: 12px; flex: none; }
  .card-front .radio-image { right: 50px; top: 90px; width: 70px; height: 170px; }
  .bottom-band { position: absolute; left: 0; right: 0; bottom: 0; height: 10px; background: var(--red); }

  /* back */
  .card-back .radio-image { left: 48px; top: 60px; width: 62px; height: 170px; }
  .back-content { position: absolute; left: 150px; top: 48px; }
  .card-back .wordmark { font-size: 36px; margin-bottom: 20px; }
  .service-list { list-style: none; }
  .service-list li { display: flex; align-items: center; gap: 8px; font-size: 10px; letter-spacing: 1px; text-transform: uppercase; margin-top: 8px; }
  .service-list li::before { content: ""; width: 5px; height: 5px; background: var(--ink); border-radius: 50%; flex: none; }
  .service-list .accent { color: var(--red); }
</style>
</head>
<body>
  <section class="card card-front">
    <div class="wordmark">TORVEX</div>
    <div class="contact-block">
      <div class="person-name">Miles Brandt</div>
      <div class="person-title">Vice President</div>
      <div class="contact-line">
        <svg viewBox="0 0 24 24" aria-hidden="true"><path fill="#d3202a" d="M6.6 10.8a15 15 0 0 0 6.6 6.6l2.2-2.2c.3-.3.7-.4 1-.2 1.1.4 2.3.6 3.6.6.6 0 1 .4 1 1V20c0 .6-.4 1-1 1A17 17 0 0 1 3 4c0-.6.4-1 1-1h3.5c.6 0 1 .4 1 1 0 1.3.2 2.5.6 3.6.1.3 0 .7-.2 1z"/></svg>
        <span>(555)-014-2290</span>
      </div>
      <div class="contact-line">
        <svg viewBox="0 0 24 24" aria-hidden="true"><rect x="2" y="5" width="20" height="14" rx="2" fill="#d3202a"/><path d="M3 6l9 7 9-7" stroke="#fff" stroke-width="2" fill="none"/></svg>
        <span>miles@torvex.example</span>
      </div>
      <div class="contact-line">
        <svg viewBox="0 0 24 24" aria-hidden="true"><circle cx="12" cy="12" r="10" fill="#d3202a"/><path d="M2 12h20M12 2c3 3 3 17 0 20M12 2c-3 3-3 17 0 20" stroke="#fff" stroke-width="1.5" fill="none"/></svg>
        <span>www.torvex.example</span>
      </div>
    </div>
    <div class="radio-image" role="img" aria-label="Handheld two-way radio photo"></div>
    <div class="bottom-band"></div>
  </section>

  <section class="card card-back">
    <div class="radio-image" role="img" aria-label="Handheld two-way radio photo"></div>
    <div class="back-content">
      <div class="wordmark">TORVEX</div>
      <ul class="service-list">
        <li><span><span class="accent">Digital</span> Communications</span></li>
        <li><span><span class="accent">Coastline</span> Fleet Relay Grid</span></li>
        <li><span><span class="accent">Cellphone</span> Coverage Enhancement</span></li>
        <li><span><span class="accent">P25 -</span> Public Safety Equipment</span></li>
        <li><span><span class="accent">Digital</span> Radio Rentals</span></li>
        <li><span><span class="accent">Dispatch</span> Consoles</span></li>
      </ul>
    </div>
  </section>
</body>
</html>
```